EAT DIRT! Packaging redesign for Moonhops Energy Bites

We are redesigning our packaging for Moonhops Energy Bites, a healthy snack for people who want to build a better world. This brand is about action, health, and authenticity
Right now we need mockups of 4 different packaging aesthetics to survey customers about. We will then pick a winner and create a final design.
The four aesthetics are:
1. Hipster-ish
2. Vaporwave/retro
3. Kid-friendly
4. Hippy Snacks
We were working with a graphic designer who unfortunately passed away. We're hoping you can pick up where he left off. He completed a mockup for the hipster aesthetic, and a concept sketch for kid friendly.
The brand archetype for moonhops is Jester/Outlaw. Moonhop enthusiasts question mainstream assumptions about the world. We want to create better systems of spiritual actualization, and have as much fun as possible doing it.
Important points for the packaging:
-Drink water, breathe air, eat dirt
-Dates, Papaya, coconut
-Simple whole food ingredients
-Soft & chewy
-Made by humans
These will be custom printed, so don't feel constrained to the brown kraft paper. it can be any color we imagine. It important to have the window on the pouch, though.
A good job on this project WILL lead to more design work for you.

```html
<!DOCTYPE html>
<html lang="en">
<head>
<meta charset="utf-8">
<title>Moonhops Energy Bites – Pouch Range</title>
<link href="https://fonts.googleapis.com/css2?family=Arimo:wght@400;700&display=swap" rel="stylesheet">
<style>
  :root {
    --page-bg: #e9e9ea;
    --ink-dark: #2b2b2b;
    --badge-green: #4f8a3c;
    --panel-white: #ffffff;

    --sun-band: #f1c331;
    --sun-logo: #e7811f;
    --sun-sky-top: #f6d45c;
    --sun-sky-bottom: #fdf3d2;
    --sun-base: #fbeec0;
    --sun-tag: #e7811f;

    --sky-band: #3fb6e6;
    --sky-logo: #1b1f6a;
    --sky-sky-top: #4dbde9;
    --sky-sky-bottom: #dff3fb;
    --sky-base: #8fd3f0;
    --sky-tag: #1f2a47;

    --clay-band: #ebbd9c;
    --clay-logo: #8b1b15;
    --clay-sky-top: #e9b996;
    --clay-sky-bottom: #fbe9dc;
    --clay-base: #edc3a5;
    --clay-tag: #3a2a22;

    --hill-green: #5e9e3f;
    --mountain: #b8876e;
    --bite-light: #b89a82;
    --bite-dark: #6b4f3a;
  }
  * { box-sizing: border-box; margin: 0; padding: 0; }
  html, body { width: 1200px; height: 713px; overflow: hidden; }
  body {
    background: var(--page-bg);
    font-family: "Arimo", Arial, sans-serif;
    position: relative;
  }
  .pouch {
    position: absolute;
    top: 100px;
    width: 290px;
    height: 510px;
    border-radius: 14px 14px 4px 4px;
    overflow: hidden;
    background: var(--base);
    box-shadow: 0 6px 18px rgba(0,0,0,.12);
  }
  .pouch--sun  { left: 90px;  --band: var(--sun-band);  --logo: var(--sun-logo);  --sky-top: var(--sun-sky-top);  --sky-bottom: var(--sun-sky-bottom);  --base: var(--sun-base);  --tag: var(--sun-tag);  --ribbon: var(--sun-logo); }
  .pouch--sky  { left: 455px; --band: var(--sky-band);  --logo: var(--sky-logo);  --sky-top: var(--sky-sky-top);  --sky-bottom: var(--sky-sky-bottom);  --base: var(--sky-base);  --tag: var(--sky-tag);  --ribbon: var(--sky-logo); }
  .pouch--clay { left: 820px; --band: var(--clay-band); --logo: var(--clay-logo); --sky-top: var(--clay-sky-top); --sky-bottom: var(--clay-sky-bottom); --base: var(--clay-base); --tag: var(--clay-tag); --ribbon: var(--badge-green); }

  .pouch__band {
    height: 72px;
    background: var(--band);
    display: flex;
    align-items: flex-end;
    justify-content: center;
    padding-bottom: 8px;
  }
  .pouch__ingredients { font-size: 11.5px; color: var(--ink-dark); letter-spacing: .2px; }

  .pouch__scene {
    position: absolute;
    top: 72px; left: 0; right: 0;
    height: 240px;
    background: linear-gradient(to bottom, var(--sky-top) 0%, var(--sky-bottom) 45%, #fff 62%, var(--mountain) 72%, var(--hill-green) 88%, #3d6b30 100%);
  }
  .pouch__lower {
    position: absolute;
    top: 312px; left: 0; right: 0; bottom: 0;
    background: linear-gradient(to bottom, var(--base) 0%, var(--base) 55%, #fff 100%);
  }
  .brand-name {
    position: absolute;
    top: 112px; left: 0; right: 0;
    text-align: center;
    font-weight: 700;
    font-size: 50px;
    color: var(--logo);
    letter-spacing: .5px;
  }
  .ribbon {
    position: absolute;
    top: 328px; left: 65px;
    width: 162px; height: 28px;
    background: var(--ribbon);
    clip-path: polygon(0 12%, 100% 0, 96% 100%, 3% 100%);
    color: #fff;
    font-weight: 700;
    font-size: 15px;
    display: flex; align-items: center; justify-content: center;
    letter-spacing: .4px;
  }
  .window {
    position: absolute;
    top: 358px; left: 36px;
    width: 206px; height: 86px;
    border-radius: 50%;
    border: 2px solid var(--logo);
    background: radial-gradient(ellipse at 55% 50%, var(--bite-light) 0%, #9a7c64 40%, var(--bite-dark) 100%);
  }
  .tagline {
    position: absolute;
    top: 446px; left: 20px;
    font-size: 12.5px;
    line-height: 15px;
    color: var(--tag);
  }
  .pouch--sun .tagline { font-weight: 700; }
  .certs {
    position: absolute;
    top: 449px; right: 14px;
    display: flex; gap: 5px;
  }
  .certs span {
    width: 18px; height: 18px;
    border: 1.5px solid var(--badge-green);
    border-radius: 50%;
  }
  .net-weight {
    position: absolute;
    top: 474px; right: 14px;
    display: flex;
    border: 1px solid var(--badge-green);
    font-size: 6.5px;
    background: #fff;
  }
  .net-weight__amount { padding: 3px 8px; color: #555; }
  .net-weight__count { padding: 3px 5px; background: var(--badge-green); color: #fff; }
</style>
</head>
<body>

  <section class="pouch pouch--sun">
    <div class="pouch__band"><p class="pouch__ingredients">• Dates • Papaya • coconut</p></div>
    <div class="pouch__scene" role="img" aria-label="Illustrated countryside with mountains, a windmill and two farmers tending a field under a sunny sky"></div>
    <div class="pouch__lower" role="img" aria-label="Soft circular bite pattern"></div>
    <h1 class="brand-name">Moonhops</h1>
    <div class="ribbon">SOFT &amp; CHEWY</div>
    <div class="window" role="img" aria-label="Window showing the energy bites inside"></div>
    <p class="tagline">Drink Water<br>Breathe Air<br>Eat Dirt</p>
    <div class="certs"><span></span><span></span><span></span><span></span></div>
    <div class="net-weight"><span class="net-weight__amount">NET WT. 9 oz (255g)</span><span class="net-weight__count">6 pack</span></div>
  </section>

  <section class="pouch pouch--sky">
    <div class="pouch__band"><p class="pouch__ingredients">• Dates • Papaya • coconut</p></div>
    <div class="pouch__scene" role="img" aria-label="Illustrated countryside with mountains, a windmill and two farmers tending a field under a blue sky"></div>
    <div class="pouch__lower" role="img" aria-label="Soft circular bite pattern"></div>
    <h1 class="brand-name">Moonhops</h1>
    <div class="ribbon">SOFT &amp; CHEWY</div>
    <div class="window" role="img" aria-label="Window showing the energy bites inside"></div>
    <p class="tagline">Drink Water<br>Breathe Air<br>Eat Dirt</p>
    <div class="certs"><span></span><span></span><span></span><span></span></div>
    <div class="net-weight"><span class="net-weight__amount">NET WT. 9 oz (255g)</span><span class="net-weight__count">6 pack</span></div>
  </section>

  <section class="pouch pouch--clay">
    <div class="pouch__band"><p class="pouch__ingredients">• Dates • Papaya • coconut</p></div>
    <div class="pouch__scene" role="img" aria-label="Illustrated countryside with mountains, a windmill and two farmers tending a field under a warm sky"></div>
    <div class="pouch__lower" role="img" aria-label="Soft circular bite pattern"></div>
    <h1 class="brand-name">Moonhops</h1>
    <div class="ribbon">SOFT &amp; CHEWY</div>
    <div class="window" role="img" aria-label="Window showing the energy bites inside"></div>
    <p class="tagline">Drink Water<br>Breathe Air<br>Eat Dirt</p>
    <div class="certs"><span></span><span></span><span></span><span></span></div>
    <div class="net-weight"><span class="net-weight__amount">NET WT. 9 oz (255g)</span><span class="net-weight__count">6 pack</span></div>
  </section>

</body>
</html>
```